Ostervik Renovations needs a website.

I need a platform for clients to go and learn about what my company does, see pictures of projects, and contact me about their projects. I am a residential remodeler specializing in general contracting services for kitchens, bathrooms, basements, additions, custom interiors, and more. I have attached my logo to be incorporated.

```html
<!DOCTYPE html>
<html lang="en">
<head>
<meta charset="utf-8">
<title>Ostervik Renovations</title>
<link href="https://fonts.googleapis.com/css2?family=Prata&family=Poppins:wght@400;500;600&display=swap" rel="stylesheet">
<style>
:root{
  --green:#6f9f6c;
  --footer:#77a875;
  --dark:#1c1c1c;
  --nav:#222222;
  --ink:#1a1a1a;
  --muted:#7a7a7a;
  --field:#f3f3f3;
  --white:#ffffff;
}
*{box-sizing:border-box;margin:0;padding:0}
html,body{width:1200px;height:3974px;overflow:hidden}
body{position:relative;background:var(--white);font-family:"Poppins",sans-serif;color:var(--ink)}
.abs{position:absolute}
.serif{font-family:"Prata",serif;font-weight:400}
.btn{position:absolute;display:flex;align-items:center;justify-content:center;background:var(--green);color:var(--white);font-size:12px;font-weight:500;text-transform:uppercase;letter-spacing:.3px}

/* hero */
.hero{left:0;top:0;width:1196px;height:657px;background:linear-gradient(100deg,#3a332c 0%,#4e463d 35%,#5c5249 55%,#3b332b 80%,#2a241f 100%)}
.hero-shade{left:0;top:0;width:1196px;height:657px;background:linear-gradient(90deg,rgba(0,0,0,.35),rgba(0,0,0,.05))}
.nav{left:54px;top:39px;width:1080px;height:78px;background:var(--nav)}
.brand{left:54px;top:39px;width:228px;height:78px;background:var(--white);display:flex;align-items:center;gap:10px;padding-left:14px}
.brand-mark{width:30px;height:30px;background:var(--green);flex:none}
.brand-name{font-size:15px;font-weight:600;line-height:1.1;color:var(--ink);text-transform:uppercase}
.nav-links{left:400px;top:73px;display:flex;gap:40px;font-size:13px;color:var(--white)}
.nav-btn{left:947px;top:65px;width:122px;height:32px;font-size:10px}
.welcome{left:80px;top:272px;color:var(--green);font-size:17px;font-weight:500}
.hero-title{left:80px;top:310px;color:var(--white);font-size:46px;letter-spacing:.5px}
.hero-text{left:84px;top:364px;width:600px;color:var(--white);font-size:14px;line-height:1.25}
.hero-btn{left:88px;top:429px;width:145px;height:36px}
.hero-btn2{left:255px;top:427px;width:147px;height:38px;border:2px solid var(--white);background:transparent}
.dots{left:570px;top:624px;display:flex;gap:8px}
.dots span{width:12px;height:12px;border-radius:50%;background:var(--white)}
.dots span.ring{background:transparent;border:2px solid var(--white)}

/* projects */
.section-title{font-size:44px;width:1200px;text-align:center}
.photo{position:absolute}
.project{position:absolute;width:517px;height:335px;display:flex;flex-direction:column;align-items:center;justify-content:center;text-align:center}
.project h3{font-family:"Prata",serif;font-weight:400;font-size:27px;margin-bottom:18px}
.project p{width:395px;font-size:11px;line-height:21px;color:var(--muted);margin-bottom:20px}
.project .btn{position:static;width:146px;height:39px}

/* about */
.about{left:0;top:2365px;width:1196px;height:506px;background:var(--dark)}
.about-photo{left:599px;top:2365px;width:597px;height:506px;background:linear-gradient(135deg,#6d6963 0%,#9a8b78 40%,#c2a27c 65%,#3a3633 100%);clip-path:ellipse(100% 95% at 100% 50%)}
.about-title{left:84px;top:2500px;color:var(--white);font-size:46px}
.about-text{left:80px;width:420px;color:var(--white);font-size:11px;line-height:17px}
.about-btn{left:80px;top:2723px;width:132px;height:33px;font-size:11px}

/* quote */
.quote-title{left:99px;top:3062px;font-size:44px}
.field{position:absolute;background:var(--field);border:1px solid #ececec;font-size:9px;color:#9a9a9a;text-transform:uppercase;padding:13px 0 0 18px}
.submit{left:99px;top:3333px;width:143px;height:34px;font-size:11px}
.test-title{left:722px;top:3062px;font-size:44px}
.stars{left:728px;top:3140px;display:flex;gap:7px}
.test-text{left:726px;top:3180px;width:345px;font-size:17px;line-height:20px;color:var(--muted)}
.avatar{left:723px;top:3328px;width:66px;height:66px;border-radius:50%;background:linear-gradient(160deg,#e8e2da,#c88f4a)}
.person{left:813px;top:3343px;font-size:15px;font-weight:600;line-height:1.1}
.person span{display:block;font-weight:400;color:var(--green);font-size:15px}

/* footer */
.footer{left:2px;top:3529px;width:1196px;height:445px;background:var(--footer)}
.foot-brand{left:116px;top:3672px;width:250px;height:87px;background:var(--white);display:flex;align-items:center;gap:12px;padding-left:20px}
.socials{left:126px;top:3790px;display:flex;gap:10px}
.socials span{width:42px;height:42px;border-radius:50%;background:var(--white)}
.foot-head{font-size:25px;color:var(--white);text-transform:uppercase}
.foot-list{list-style:none;color:var(--white);font-size:18px}
.foot-list li{display:flex;align-items:center;gap:10px;height:39px}
.contact li{height:auto;align-items:flex-start;margin-bottom:19px;line-height:22px}
.rule{left:123px;top:3888px;width:969px;height:1px;background:rgba(255,255,255,.7)}
.copy{left:0;top:3914px;width:1200px;text-align:center;color:var(--white);font-size:15px}
</style>
</head>
<body>

<header>
  <div class="abs hero" role="img" aria-label="Photo of a warmly lit renovated living and dining room"></div>
  <div class="abs hero-shade"></div>
  <nav class="abs nav"></nav>
  <div class="abs brand"><span class="brand-mark"></span><span class="brand-name">Ostervik<br>Renovations</span></div>
  <div class="abs nav-links"><span>HOME</span><span>ABOUT</span><span>SERVICES</span><span>PROJECTS</span><span>CONTACT</span></div>
  <a class="btn nav-btn">Get a quote</a>
  <p class="abs welcome">Welcome to</p>
  <h1 class="abs serif hero-title">OSTERVIK RENOVATIONS</h1>
  <p class="abs hero-text">Lorem ipsum dolor sit amet, consectetur adipiscing elit, sed do eiusmod tempor incididunt ut labore et dolore magna aliqua.</p>
  <a class="btn hero-btn">Get a quote</a>
  <a class="btn hero-btn2">Read more</a>
  <div class="abs dots"><span></span><span class="ring"></span><span></span></div>
</header>

<section>
  <h2 class="abs serif section-title" style="top:745px">RECENT PROJECTS</h2>

  <div class="photo" style="left:86px;top:873px;width:516px;height:335px;background:linear-gradient(135deg,#6b5240,#d9cbb5 50%,#8a6a4c)" role="img" aria-label="Photo of a modern interior hallway with marble floor"></div>
  <div class="project" style="left:602px;top:873px">
    <h3>INTERIOR PROJECT</h3>
    <p>We specialize in turning outdated kitchens and bathrooms into beautiful, functional spaces you'll love. Whether you're dreaming of a sleek modern kitchen, a cozy farmhouse bath, or a luxurious spa-like retreat, our team delivers exceptional craftsmanship and personalized service.</p>
    <a class="btn">View details</a>
  </div>

  <div class="project" style="left:86px;top:1233px">
    <h3>KITCHEN PROJECT</h3>
    <p>We specialize in turning outdated kitchens and bathrooms into beautiful, functional spaces you'll love. Whether you're dreaming of a sleek modern kitchen, a cozy farmhouse bath, or a luxurious spa-like retreat, our team delivers exceptional craftsmanship and personalized service.</p>
    <a class="btn">View details</a>
  </div>
  <div class="photo" style="left:603px;top:1208px;width:516px;height:337px;background:linear-gradient(135deg,#e9e4dc,#f4efe6 45%,#9c7a58 80%,#6a6a62)" role="img" aria-label="Photo of a bright kitchen with dining table and bar stools"></div>

  <div class="photo" style="left:86px;top:1545px;width:516px;height:334px;background:linear-gradient(120deg,#5d5d5b,#b7b2aa 45%,#a2794e 70%,#7d8da0)" role="img" aria-label="Photo of a modern bathroom with wooden vanity and city view"></div>
  <div class="project" style="left:602px;top:1560px">
    <h3>BATHROOM PROJECT</h3>
    <p>We specialize in turning outdated kitchens and bathrooms into beautiful, functional spaces you'll love. Whether you're dreaming of a sleek modern kitchen, a cozy farmhouse bath, or a luxurious spa-like retreat, our team delivers exceptional craftsmanship and personalized service.</p>
    <a class="btn">View details</a>
  </div>

  <div class="project" style="left:70px;top:1905px">
    <h3>KITCHEN RENOVATION</h3>
    <p>We specialize in turning outdated kitchens and bathrooms into beautiful, functional spaces you'll love. Whether you're dreaming of a sleek modern kitchen, a cozy farmhouse bath, or a luxurious spa-like retreat, our team delivers exceptional craftsmanship and personalized service.</p>
    <a class="btn">View details</a>
  </div>
  <div class="photo" style="left:603px;top:1879px;width:515px;height:335px;background:linear-gradient(135deg,#c9a88a,#e6d2bc 45%,#c46a2a 70%,#3f3a36)" role="img" aria-label="Photo of a sunny kitchen counter with gas stove and plant"></div>
</section>

<section>
  <div class="abs about"></div>
  <div class="abs about-photo" role="img" aria-label="Photo of a dark modern kitchen with wooden table and black chairs"></div>
  <h2 class="abs serif about-title">ABOUT US</h2>
  <p class="abs about-text" style="top:2568px">We specialize in turning outdated kitchens and bathrooms into beautiful, functional spaces you'll love. Whether you're dreaming of a sleek modern kitchen, a cozy farmhouse bath, or a luxurious spa-like retreat, our team delivers exceptional craftsmanship and personalized service.</p>
  <p class="abs about-text" style="top:2643px">We specialize in turning outdated kitchens and bathrooms into beautiful, functional spaces you'll love. Whether you're dreaming of a sleek modern kitchen, a cozy farmhouse bath, or a luxurious spa-like retreat, our team delivers exceptional craftsmanship and personalized service.</p>
  <a class="btn about-btn">Read more</a>
</section>

<section>
  <h2 class="abs serif quote-title">GET A QUOTE</h2>
  <div class="field" style="left:85px;top:3163px;width:255px;height:32px">Full name</div>
  <div class="field" style="left:353px;top:3163px;width:256px;height:32px">Email address</div>
  <div class="field" style="left:85px;top:3206px;width:255px;height:32px">Phone number</div>
  <div class="field" style="left:353px;top:3206px;width:256px;height:32px">Select service</div>
  <div class="field" style="left:85px;top:3253px;width:524px;height:62px">Additional message</div>
  <a class="btn submit">Submit details</a>

  <h2 class="abs serif test-title">TESTIMONIALS</h2>
  <div class="abs stars">
    <svg width="160" height="22" viewBox="0 0 160 22" aria-label="Five stars">
      <g fill="var(--green)">
        <path id="st" d="M11 1l3 7h7l-6 4.5 2.3 7.5L11 15.5 4.7 20 7 12.5 1 8h7z"/>
        <use href="#st" x="32"/><use href="#st" x="64"/><use href="#st" x="96"/><use href="#st" x="128"/>
      </g>
    </svg>
  </div>
  <p class="abs test-text">The sales dashboards are fantastic! They provide clear, real-time insights into our performance, which has sparked healthy competition within our office. Everyone is motivated to reach their targets, and our sales numbers have never been better!</p>
  <div class="abs avatar" role="img" aria-label="Portrait photo of the client"></div>
  <p class="abs person">DANA K.<span>Owner</span></p>
</section>

<footer>
  <div class="abs footer"></div>
  <div class="abs foot-brand"><span class="brand-mark"></span><span class="brand-name" style="font-size:17px">Ostervik<br>Renovations</span></div>
  <div class="abs socials"><span></span><span></span><span></span><span></span></div>

  <h3 class="abs foot-head" style="left:461px;top:3630px">Quick links</h3>
  <ul class="abs foot-list" style="left:463px;top:3683px">
    <li><svg width="20" height="20" viewBox="0 0 20 20"><circle cx="10" cy="10" r="8.5" fill="none" stroke="#fff" stroke-width="1.6"/><path d="M6 10h8M10.5 6.5L14 10l-3.5 3.5" fill="none" stroke="#fff" stroke-width="1.6"/></svg>HOME</li>
    <li><svg width="20" height="20" viewBox="0 0 20 20"><circle cx="10" cy="10" r="8.5" fill="none" stroke="#fff" stroke-width="1.6"/><path d="M6 10h8M10.5 6.5L14 10l-3.5 3.5" fill="none" stroke="#fff" stroke-width="1.6"/></svg>ABOUT</li>
    <li><svg width="20" height="20" viewBox="0 0 20 20"><circle cx="10" cy="10" r="8.5" fill="none" stroke="#fff" stroke-width="1.6"/><path d="M6 10h8M10.5 6.5L14 10l-3.5 3.5" fill="none" stroke="#fff" stroke-width="1.6"/></svg>PRICING</li>
    <li><svg width="20" height="20" viewBox="0 0 20 20"><circle cx="10" cy="10" r="8.5" fill="none" stroke="#fff" stroke-width="1.6"/><path d="M6 10h8M10.5 6.5L14 10l-3.5 3.5" fill="none" stroke="#fff" stroke-width="1.6"/></svg>CONTACT</li>
  </ul>

  <h3 class="abs foot-head" style="left:793px;top:3630px">Contact</h3>
  <ul class="abs foot-list contact" style="left:797px;top:3707px">
    <li><svg width="24" height="24" viewBox="0 0 24 24"><circle cx="12" cy="12" r="12" fill="#fff"/><path d="M8.5 6.5l2 2.5-1.2 1.5c.8 1.8 2.4 3.4 4.2 4.2l1.5-1.2 2.5 2-1.5 2c-4.5-.5-8.5-4.5-9-9z" fill="var(--footer)"/></svg>+1 555-014-2290</li>
    <li><svg width="24" height="24" viewBox="0 0 24 24"><circle cx="12" cy="12" r="12" fill="#fff"/><rect x="6.5" y="8" width="11" height="8" fill="var(--footer)"/><path d="M6.5 8l5.5 4.5L17.5 8" fill="none" stroke="#fff" stroke-width="1.2"/></svg>hello@ostervikreno.com</li>
    <li><svg width="24" height="24" viewBox="0 0 24 24"><circle cx="12" cy="12" r="12" fill="#fff"/><path d="M12 5.5a4.5 4.5 0 0 1 4.5 4.5c0 3.3-4.5 8-4.5 8s-4.5-4.7-4.5-8A4.5 4.5 0 0 1 12 5.5z" fill="var(--footer)"/><circle cx="12" cy="10" r="1.6" fill="#fff"/></svg><span>318 Harbor Lane<br>Brightwater, SC 29000, USA</span></li>
  </ul>

  <div class="abs rule"></div>
  <p class="abs copy">Copyright© 2025 Ostervik renovations,, All rights reserved.</p>
</footer>

</body>
</html>
```